Package Design for 15 lines of Tea

I need design variations for 15 different Tea lines.
The tea will be packaged in Tin cylinders.
I have attached several pictures to show you an example of the display we are modelling after along with other references.
The 15 tea lines are:
Study Tea
Ingredients: Brazilian Mate, Mint
Energy Boost Tea
Ingredients: Yunnan Coffee, Dark Puer
Relaxation Tea
Ingredients: Lotus Flower, South African Rooibos
Beauty Tea
Ingredients: Rose, Chrysanthemum, Red Dates, Huangqi
Sore Throat Tea
Ingredients: Honeysuckle, Pang Da Hai, Chamomile, Licorice Root
Get Well Tea
Ingredients: Ginger, Rooibos, Orange peel, Chinese Angelica
Diet Tea
Ingredients: Puer, Hibiscus, Lemongrass, Lotus Plumule
Bedtime Tea
Ingredients: Apple, Orange, Chamomile
South African Rooibos Tea
(pure)
Brazilian Yerba Mate Tea
(pure)
Long Jing Green Tea
(pure)
Darjeeling Black Tea
(pure)
Nepal Golden Tea
(Pure)
Bai Mu Dan White Tea
(pure)
Phoenix Oolong Tea
(pure)
Every Tea Blend should have three unique symbols that describe the purpose and theme of the blend. (!!Please don't make specific reference to the ingredients of the blends because some of these ingredients may be changed later. Stick to focusing on the intended purpose of the tea blend!!)
I would like the symbols to keep the same brushlike style that is consistent with our company logo.
Please keep the three block structure. I suggest keeping to just one color per tea blend. This will help each blend stand out between one another. I have a sample of the "Diet Tea" attached that I did myself to give you an idea of the structure I'm looking for, but obviously it's just my amateur version. Hope you can make them look far more appealing.
The ultimate goal is to build a picture language unique to our brand. As more products are released, we intend to potentially have hundreds of symbols, each with it's own meaning. So it would be nice when you present your pictures if you explain its intended meaning or message.
Deminsions:
Cylinder type 1: 82mm*38mmH
circular labels (along with your design) will be placed on the cap of product, and then the cylinder will be slanted on it's side to display the cap towards the customer.
Cylinder type 2: 65mm*152mmH
the labels will be placed on the side of the cylinder. In this version, try lining the three symbols in a vertical position. If this looks awful to you then feel free to go back to the horizontal style, but it would be nice to see what the vertical version looks like for reference.
Updates
Due to the scope of this project, please take note that I just increased my budget an additional 500 dollars more.
I also just added a 100 dollar second place prize. Don't want to see hard work unrewarded.
Feel free to send a few samples and I will provide prompt feedback. Please don't feel that you must submit all 15 lines at the same time.
Project Deadline Extended
Reason: I am extending the deadline as I feel there are more detailed revisions that need to be made until final selection.
Target Market(s)
Middle to Upper Class Consumers in China
Industry/Entity Type
It Company
Other font styles liked:
- font similar to font on company logo
Requirements
Must have
- Tea Designs must be in harmony with company logo and theme.
Should not have
- Avoid using Chinese characters as symbols. They may seem cool to westerners, but it's tacky for Chinese consumers.

```html
<!DOCTYPE html>
<html lang="en">
<head>
<meta charset="utf-8">
<title>Hollin Tea – Cap Labels</title>
<link rel="stylesheet" href="https://fonts.googleapis.com/css2?family=Space+Mono:wght@400;700&display=swap">
<style>
  :root {
    --page: #ffffff;
    --ink: #0b0b0b;
    --relax: #8fb3db;
    --bedtime: #e0a526;
    --energy: #c3161c;
    --symbol-relax: #7fa6cc;
    --symbol-bedtime: #c9921c;
    --symbol-energy: #b3141a;
    --ingredient-ink: rgba(11, 11, 11, 0.72);
    --label-size: 340px;
  }
  * { box-sizing: border-box; margin: 0; padding: 0; }
  html, body {
    width: 1200px;
    height: 600px;
    overflow: hidden;
    background: var(--page);
    font-family: "Space Mono", monospace;
  }
  .label-row {
    width: 1200px;
    height: 600px;
    display: flex;
    align-items: center;
    justify-content: center;
    gap: 50px;
  }
  .cap-label {
    width: var(--label-size);
    height: var(--label-size);
    border-radius: 50%;
    overflow: hidden;
    display: grid;
    grid-template-columns: 1fr 1fr;
    color: var(--ink);
  }
  .cap-label--relax   { --accent: var(--relax);   --symbol: var(--symbol-relax); }
  .cap-label--bedtime { --accent: var(--bedtime); --symbol: var(--symbol-bedtime); }
  .cap-label--energy  { --accent: var(--energy);  --symbol: var(--symbol-energy); }

  .symbol-half {
    background: var(--ink);
    display: flex;
    align-items: center;
    justify-content: flex-end;
    padding: 40px 16px 0 0;
  }
  .hero-symbol {
    width: 104px;
    height: 46px;
    border-radius: 8px;
    background: var(--symbol);
  }
  .info-half {
    background: var(--accent);
    padding: 58px 0 0 12px;
    display: flex;
    flex-direction: column;
  }
  .brand {
    font-size: 11px;
    font-weight: 700;
    line-height: 1;
  }
  .symbol-blocks {
    display: flex;
    gap: 4px;
    margin-top: 5px;
  }
  .symbol-block {
    width: 18px;
    height: 18px;
    background: var(--ink);
    display: flex;
    align-items: center;
    justify-content: center;
  }
  .symbol-block span {
    width: 10px;
    height: 10px;
    border-radius: 2px;
    background: var(--symbol);
  }
  .blend-name {
    margin-top: 34px;
    font-size: 21px;
    font-weight: 700;
    line-height: 1.05;
    letter-spacing: -0.5px;
  }
  .ingredients {
    margin-top: 8px;
    font-size: 9px;
    line-height: 1.35;
    width: 130px;
    color: var(--ingredient-ink);
  }
</style>
</head>
<body>
  <main class="label-row">
    <section class="cap-label cap-label--relax">
      <div class="symbol-half">
        <div class="hero-symbol" role="img" aria-label="Brush-stroke wave symbol for relaxation"></div>
      </div>
      <div class="info-half">
        <p class="brand">Hollin Tea</p>
        <div class="symbol-blocks">
          <div class="symbol-block" role="img" aria-label="Relaxation symbol one"><span></span></div>
          <div class="symbol-block" role="img" aria-label="Relaxation symbol two"><span></span></div>
          <div class="symbol-block" role="img" aria-label="Relaxation symbol three"><span></span></div>
        </div>
        <h2 class="blend-name">Relaxation<br>tea</h2>
        <p class="ingredients">Ingredients:<br>Lotus Flower,<br>South African<br>Rooibos</p>
      </div>
    </section>

    <section class="cap-label cap-label--bedtime">
      <div class="symbol-half">
        <div class="hero-symbol" role="img" aria-label="Brush-stroke crescent moon and stars symbol for bedtime"></div>
      </div>
      <div class="info-half">
        <p class="brand">Hollin Tea</p>
        <div class="symbol-blocks">
          <div class="symbol-block" role="img" aria-label="Bedtime symbol one"><span></span></div>
          <div class="symbol-block" role="img" aria-label="Bedtime symbol two"><span></span></div>
          <div class="symbol-block" role="img" aria-label="Bedtime symbol three"><span></span></div>
        </div>
        <h2 class="blend-name">Bedtime<br>tea</h2>
        <p class="ingredients">Ingredients:<br>Apple,<br>Orange,<br>Chamomile</p>
      </div>
    </section>

    <section class="cap-label cap-label--energy">
      <div class="symbol-half">
        <div class="hero-symbol" role="img" aria-label="Brush-stroke lightning bolt symbol for energy"></div>
      </div>
      <div class="info-half">
        <p class="brand">Hollin Tea</p>
        <div class="symbol-blocks">
          <div class="symbol-block" role="img" aria-label="Energy symbol one"><span></span></div>
          <div class="symbol-block" role="img" aria-label="Energy symbol two"><span></span></div>
          <div class="symbol-block" role="img" aria-label="Energy symbol three"><span></span></div>
        </div>
        <h2 class="blend-name">Energy<br>Boost<br>tea</h2>
        <p class="ingredients">Ingredients:<br>Yunnan Coffee,<br>Dark Puer</p>
      </div>
    </section>
  </main>
</body>
</html>
```